Sales Flyer Design

Create a Flyer front and back that highlights the different things we do
We do Addition, basements, kitchens, bathrooms, concrete, siding, Roofing.

We want to highlight that we are licensed Electrical Contractor and Plumbers.
Use our Logo attached keeping color scheme mainly our company colors. We are looking for an attention grabbing but easy read for homeowners.

```html
<!DOCTYPE html>
<html lang="en">
<head>
<meta charset="utf-8">
<title>Northvale Remodeling &amp; Restoration – Flyer</title>
<link rel="stylesheet" href="https://fonts.googleapis.com/css2?family=Orbitron:wght@600;700&family=Outfit:wght@300;400;500;600&display=swap">
<style>
  :root{
    --orange:#e8612c;
    --dark:#151515;
    --light:#f2f2f2;
    --white:#ffffff;
    --ink:#1d1d1d;
    --display:'Orbitron', sans-serif;
    --body:'Outfit', sans-serif;
  }
  *{margin:0;padding:0;box-sizing:border-box}
  html,body{width:1200px;height:779px;overflow:hidden;background:#fff}
  .flyer{position:relative;width:1200px;height:779px;font-family:var(--body);overflow:hidden}
  .panel{position:absolute;top:0;height:779px;width:600px;overflow:hidden}
  .panel--front{left:0;background:var(--light);color:var(--ink)}
  .panel--back{left:598px;width:602px;background:var(--dark);color:var(--white)}

  .brand{position:absolute;left:40px;top:44px;width:124px;text-align:center}
  .brand__name{font-family:var(--body);font-weight:600;font-size:23px;letter-spacing:.5px;line-height:1}
  .brand__tag{font-family:var(--body);font-weight:600;font-size:7.2px;letter-spacing:.3px;margin-top:6px;border-top:1px solid currentColor;padding-top:3px;white-space:nowrap}

  .headline{position:absolute;left:245px;top:34px;font-family:var(--display);font-weight:700;font-size:23.5px;line-height:28.5px;white-space:nowrap}
  .headline em{font-style:normal;color:var(--orange)}
  .accent-bar{position:absolute;top:40px;width:10px;height:73px;background:var(--orange)}

  .photo{position:absolute}
  .frame{position:absolute;border:1px solid var(--orange)}

  .services{position:absolute;left:40px;top:106px;width:167px;height:283px;background:var(--orange);padding:12px 14px}
  .services h2{font-family:var(--display);font-weight:700;font-size:17px;color:var(--white);margin-bottom:12px;white-space:nowrap}
  .services li{list-style:none;font-size:10px;line-height:11px;color:#f6b495;margin-bottom:10.5px}
  .services li b{color:var(--white);font-weight:500}

  .section-title{position:absolute;font-family:var(--display);font-weight:700;font-size:15.5px;line-height:20px;color:var(--orange);white-space:nowrap}
  .section-title--compact{font-size:13px}

  .feature{position:absolute;display:flex;align-items:center;gap:8px;font-size:10px;font-weight:500;white-space:nowrap}
  .icon{position:relative;width:30px;height:30px;flex:none}
  .icon::after{content:"";position:absolute;left:2px;top:2px;width:30px;height:30px;border:1px solid var(--orange)}
  .icon svg{position:relative;z-index:1;display:block}
  .feature small{display:block;font-size:10px;font-weight:300;margin-top:4px}

  .copy{position:absolute;font-size:10.6px;line-height:15.8px;font-weight:300}
  .cta{position:absolute;font-size:13px;font-weight:600;white-space:nowrap}

  .band{position:absolute;left:0;top:683px;height:96px}
  .phone{position:absolute;top:699px;display:flex;align-items:center;gap:11px;font-family:var(--display);font-weight:600;font-size:27px;color:var(--white);white-space:nowrap}
  .phone__icon{width:32px;height:32px;border:2px solid currentColor;border-radius:6px;display:flex;align-items:center;justify-content:center}

  .contact{position:absolute;top:636px;width:167px;height:143px;padding:15px 18px}
  .contact h2{font-family:var(--display);font-weight:700;font-size:16px;margin-bottom:9px;white-space:nowrap}
  .contact p{font-size:10px;line-height:15.7px;font-weight:500;white-space:nowrap}

  .testimonial{position:absolute;left:39px;top:267px;width:206px;height:122px;background:var(--white);color:var(--ink);padding:14px 14px}
  .testimonial blockquote{font-size:13px;line-height:19.7px;font-weight:300}
  .testimonial cite{display:block;font-style:normal;font-family:var(--display);font-weight:600;font-size:8.5px;color:var(--orange);margin-top:7px;white-space:nowrap}
</style>
</head>
<body>
<main class="flyer">

  <section class="panel panel--front">
    <div class="brand">
      <div class="brand__name">Northvale</div>
      <div class="brand__tag">REMODELING &amp; RESTORATION</div>
    </div>
    <h1 class="headline">YOUR <em>ONE-STOP</em> HOME<br>TRANSFORMATION<br>EXPERTS!</h1>
    <div class="accent-bar" style="left:589px"></div>

    <div class="photo" role="img" aria-label="Modern living room with sofa, green armchair and floating staircase" style="left:0;top:134px;width:600px;height:192px;background:linear-gradient(100deg,#6d6a66 0%,#a29a91 35%,#cfc7bd 60%,#b9aea0 80%,#8a7f72 100%)"></div>

    <div class="frame" style="left:20px;top:222px;width:207px;height:190px"></div>
    <div class="services">
      <h2>WHAT WE DO</h2>
      <ul>
        <li><b>Additions |</b> Expand your space, elevate your lifestyle</li>
        <li><b>Basements |</b> From unfinished to unforgettable</li>
        <li><b>Kitchens |</b> Modern, functional, and stunning</li>
        <li><b>Bathrooms |</b> Relax in spa-like comfort</li>
        <li><b>Concrete Work |</b> Durable &amp; precise flatwork and foundations</li>
        <li><b>Siding |</b> Boost curb appeal with quality finishes</li>
        <li><b>Roofing |</b> Weather-resistant protection you can count on</li>
      </ul>
    </div>

    <h2 class="section-title section-title--compact" style="left:370px;top:358px">WHY CHOOSE NORTHVALE?</h2>

    <div class="feature" style="left:371px;top:386px">
      <div class="icon"><svg width="30" height="30"><rect width="30" height="30" fill="#e8612c"/><path d="M9 7h9l4 4v12H9z M13 12h6 M13 15h6 M13 18h4" fill="none" stroke="#fff" stroke-width="1.2"/></svg></div>
      Fully Licensed &amp; Insured
    </div>
    <div class="feature" style="left:371px;top:424px">
      <div class="icon"><svg width="30" height="30"><rect width="30" height="30" fill="#e8612c"/><path d="M8 22l12-12 M10 9l12 13 M19 8l3 3" fill="none" stroke="#fff" stroke-width="1.4"/></svg></div>
      High-Quality Craftsmanship
    </div>
    <div class="feature" style="left:371px;top:461px">
      <div class="icon"><svg width="30" height="30"><rect width="30" height="30" fill="#e8612c"/><path d="M8 6h11v17H8z M11 10h5 M11 13h5 M11 16h3" fill="none" stroke="#fff" stroke-width="1.2"/><circle cx="20" cy="20" r="3.5" fill="#e8612c" stroke="#fff" stroke-width="1.2"/></svg></div>
      Transparent Quotes &amp; Timelines
    </div>
    <div class="feature" style="left:371px;top:498px">
      <div class="icon"><svg width="30" height="30"><rect width="30" height="30" fill="#e8612c"/><path d="M15 20s-5-5-5-8a5 5 0 0 1 10 0c0 3-5 8-5 8z M8 24h14" fill="none" stroke="#fff" stroke-width="1.3"/><circle cx="15" cy="12" r="1.7" fill="#fff"/></svg></div>
      Locally Owned, Customer-Focused
    </div>

    <h2 class="section-title" style="left:40px;top:460px">LICENSED ELECTRICAL &amp;<br>PLUMBING CONTRACTORS</h2>
    <p class="copy" style="left:40px;top:514px">Don’t gamble with safety and compliance.<br>We’re certified, experienced, and code-compliant —<br>giving you peace of mind on every project.</p>
    <p class="cta" style="left:40px;top:580px">Call us today for a FREE estimate!</p>

    <div class="photo" role="img" aria-label="Electrician working on a breaker panel" style="left:319px;top:555px;width:281px;height:128px;background:linear-gradient(110deg,#c9c9c7 0%,#a9acae 45%,#4a4c4f 75%,#2a2a2a 100%)"></div>

    <div class="band" style="width:600px;background:var(--dark)"></div>
    <div class="phone" style="left:40px">
      <span class="phone__icon" style="color:var(--orange)"><svg width="18" height="18" viewBox="0 0 24 24"><path d="M6 3l3 0 2 5-2 1.5a11 11 0 0 0 5.5 5.5L16 13l5 2v3a2 2 0 0 1-2 2A16 16 0 0 1 4 5a2 2 0 0 1 2-2z" fill="none" stroke="#e8612c" stroke-width="1.8"/></svg></span>
      (555) 014-2730
    </div>

    <div class="frame" style="left:377px;top:616px;width:207px;height:200px"></div>
    <div class="contact" style="left:396px;background:var(--orange);color:var(--white)">
      <h2>CONTACT US</h2>
      <p style="color:var(--ink)">Serving Iowa<br>(555) 014-2730<br>www.northvalehomes.com<br>Follow us: @NorthvaleRemodel</p>
    </div>
  </section>

  <section class="panel panel--back">
    <div class="brand" style="left:39px">
      <div class="brand__name">Northvale</div>
      <div class="brand__tag">REMODELING &amp; RESTORATION</div>
    </div>
    <h1 class="headline" style="left:244px">YOUR <em>ONE-STOP</em> HOME<br>TRANSFORMATION<br>EXPERTS!</h1>
    <div class="accent-bar" style="left:590px"></div>

    <div class="photo" role="img" aria-label="Before and after of a renovated hallway and bathroom" style="left:0;top:134px;width:602px;height:192px;background:linear-gradient(90deg,#c49a6e 0%,#b47a52 30%,#d7cdc2 50%,#e9e9ea 70%,#dcdcdd 100%)"></div>

    <div class="frame" style="left:20px;top:305px;width:248px;height:107px"></div>
    <div class="testimonial">
      <blockquote>“Northvale remodeled our kitchen and bathroom — clean work, on time, and stress-free! Highly recommended.”</blockquote>
      <cite>— DANA R., HAPPY HOMEOWNER</cite>
    </div>

    <h2 class="section-title" style="left:299px;top:354px">YOUR VISION. OUR MISSION.</h2>
    <p class="copy" style="left:299px;top:387px;width:265px;color:#e4e4e4">At Northvale Remodeling &amp; Restoration, we believe every home has the potential to be extraordinary. Whether you’re looking to update a single room or reimagine your entire home, our expert team is ready to deliver results that exceed expectations.</p>
    <p class="cta" style="left:299px;top:485px">Call us today for a FREE estimate!</p>

    <h2 class="section-title" style="left:40px;top:455px">LICENSED<br>PROFESSIONALS<br>ON STAFF</h2>

    <div class="feature" style="left:41px;top:529px">
      <div class="icon"><svg width="30" height="30"><rect width="30" height="30" fill="#e8612c"/><rect x="9" y="7" width="12" height="16" fill="none" stroke="#fff" stroke-width="1.2"/><path d="M16 10l-3 5h4l-3 5" fill="none" stroke="#fff" stroke-width="1.2"/></svg></div>
      <div>Electrical Contractor:<small>Safe, efficient wiring &amp; installations</small></div>
    </div>
    <div class="feature" style="left:41px;top:585px">
      <div class="icon"><svg width="30" height="30"><rect width="30" height="30" fill="#e8612c"/><path d="M7 14l8-7 8 7 M9 13v10h12V13 M13 23v-5h4v5" fill="none" stroke="#fff" stroke-width="1.2"/></svg></div>
      <div>Plumbing Contractor:<small>Code-compliant and leak-free systems</small></div>
    </div>

    <div class="photo" role="img" aria-label="Plumber fitting pipes under a sink" style="left:319px;top:555px;width:283px;height:128px;background:linear-gradient(110deg,#e8e8e8 0%,#cfcfcf 35%,#8e8e90 60%,#2f3440 100%)"></div>

    <div class="band" style="width:602px;background:var(--orange)"></div>
    <div class="phone" style="left:39px">
      <span class="phone__icon" style="color:var(--dark)"><svg width="18" height="18" viewBox="0 0 24 24"><path d="M6 3l3 0 2 5-2 1.5a11 11 0 0 0 5.5 5.5L16 13l5 2v3a2 2 0 0 1-2 2A16 16 0 0 1 4 5a2 2 0 0 1 2-2z" fill="none" stroke="#151515" stroke-width="1.8"/></svg></span>
      (555) 014-2730
    </div>

    <div class="frame" style="left:377px;top:616px;width:207px;height:200px"></div>
    <div class="contact" style="left:396px;background:var(--white);color:var(--orange)">
      <h2>CONTACT US</h2>
      <p style="color:var(--ink)">Serving Iowa<br>(555) 014-2730<br>www.northvalehomes.com<br>Follow us: @NorthvaleRemodel</p>
    </div>
  </section>

</main>
</body>
</html>
```